Verpackungsdesign für CBD-Öl
Zielgruppe
CBD Produkte
Aufgabenstellung
Erstellung eines Designs für eine Verpackung von CBD-Öl. Die Verpackung sollte sich von den üblichen CBD Verpackungen abheben, mit Logo,, Hintergrund und Farben meiner Webseite sollte gearbeitet werden siehe Foto.
Design sollte sehr edel und cool ausschauen, nicht wie die meisten CBD Verpackungen. Eure Kreativität könnt Ihr freien Lauf lassen. Wir lassen uns überraschen.
Größe der Faltschachtel: Länge 27 mm, Breite 28 mm, Höhe 90 mm
Erstellung eines Design für eine Faltschachtel mit 4 verschiedenen Inhaltsangaben.
Das Grunddesign der Verpackung ist immer das gleiche, nur die Inhaltsangabe an Cannabidiol variiert.
10 % 1000MG, 15 % 1500MG, 20 % 2000MG, 30 % 3000MG
Kornwiese sollte im Vordergrund stehen und der Hintergrund siehe Bild!
Was draufstehen sollte
Vegan & Glutenfrei
Vollspektrum
CBD Premium Hanföl
Nicht zum Verzehr geeignet
Duftöl
Siehe Bild von Sarn, die Inhaltsstoffe bitte freihalten, da wir unterschiedliche Inhaltsstoffe/ Geschmacksrichtungen haben.
Erstellung Design für das Etikett für die 10-ml-Flasche.
Größe Etikett: Länge: 85 mm, Höhe: 30 mm
Das Grunddesign für das Label der 10-ml-Flasche ist immer das gleiche. Jedoch auch hier variiert die Inhaltsangabe von Cannabidiol.
10% 15% 20% und 30%
Auch unser Firmenlogo KORNWIESE können wir Ihnen in anderen Größen senden.
Sie können uns auch schreiben, um weitere Fragen abzuklären.
Gutes designen.

```html
<!DOCTYPE html>
<html lang="de">
<head>
<meta charset="utf-8">
<title>Kornwiese – Faltschachtel CBD Hanföl</title>
<link href="https://fonts.googleapis.com/css2?family=Barlow+Condensed:wght@400;500;600&family=Open+Sans:wght@700&display=swap" rel="stylesheet">
<style>
  :root {
    --page: #d9d7d1;
    --panel: #1d1d1d;
    --panel-light: #2a2a2a;
    --panel-mid: #242424;
    --gold: #d99a2b;
    --gold-light: #f2c55a;
    --green: #4f8c2f;
    --cream: #efe5c6;
    --white: #ffffff;
    --black: #0b0b0b;
  }
  * { margin: 0; padding: 0; box-sizing: border-box; }
  html, body { width: 1200px; height: 800px; overflow: hidden; background: var(--page); }
  body { font-family: "Barlow Condensed", "Arial Narrow", sans-serif; }
  .canvas { position: relative; width: 1200px; height: 800px; }
  .dieline { position: absolute; inset: 0; }
  .t { position: absolute; white-space: nowrap; line-height: 1.2; }

  .brand { color: var(--cream); font-weight: 500; letter-spacing: 1px; }
  .brand-flap { left: 599px; width: 158px; top: 86px; text-align: center; font-size: 19px; }
  .brand-side { left: 296px; width: 134px; top: 424px; text-align: center; font-size: 18px; }
  .brand-front { left: 694px; top: 180px; width: 56px; height: 313px; }
  .brand-front span {
    position: absolute; left: 50%; top: 50%;
    transform: translate(-50%, -50%) rotate(-90deg);
    font-size: 52px; letter-spacing: 3px; line-height: 1;
  }
  .est-front { left: 648px; top: 270px; width: 20px; height: 160px; }
  .est-front span {
    position: absolute; left: 50%; top: 50%;
    transform: translate(-50%, -50%) rotate(-90deg);
    font-size: 12px; letter-spacing: 3px; color: var(--cream);
  }

  .notice { color: var(--gold); font-size: 13.5px; }
  .hint { color: var(--gold); font-size: 9.6px; line-height: 1.6; }

  .claim { color: var(--gold); font-size: 12px; }
  .claim-icon { position: absolute; width: 18px; height: 18px; border: 1.5px solid var(--gold); border-radius: 50%; }
  .bullets { color: var(--gold); font-size: 9.6px; line-height: 1.65; }
  .bullets span { color: var(--gold); margin-right: 4px; }
  .ingredients { color: var(--gold); font-size: 9.6px; line-height: 1.6; }

  .premium { color: var(--gold); font-size: 13px; font-weight: 600; font-family: "Open Sans", sans-serif; }
  .product { font-size: 24px; }
  .product b { color: var(--green); font-family: "Open Sans", sans-serif; font-weight: 700; }
  .product em { font-style: normal; color: var(--gold); font-weight: 400; }
  .percent { color: var(--gold); font-size: 27px; font-family: "Open Sans", sans-serif; font-weight: 700; }
  .spectrum { color: var(--cream); font-size: 12px; line-height: 1.35; }
  .volume { color: var(--gold); font-size: 19px; }

  .batch { color: var(--white); font-size: 13.5px; line-height: 1.7; }
  .batch-field { position: absolute; left: 610px; top: 763px; width: 134px; height: 30px; background: var(--white); }
</style>
</head>
<body>
<div class="canvas">

  <svg class="dieline" width="1200" height="800" viewBox="0 0 1200 800" aria-hidden="true">
    <defs>
      <linearGradient id="goldBand" x1="0" y1="1" x2="1" y2="0">
        <stop offset="0" stop-color="#7a4a08"/>
        <stop offset="0.35" stop-color="#f4b935"/>
        <stop offset="0.6" stop-color="#c67c12"/>
        <stop offset="1" stop-color="#5a3505"/>
      </linearGradient>
      <clipPath id="netClip">
        <rect x="599" y="10" width="158" height="154"/>
        <rect x="290" y="163" width="619" height="515"/>
      </clipPath>
    </defs>
    <!-- flaps -->
    <rect x="599" y="678" width="158" height="122" fill="var(--black)"/>
    <g clip-path="url(#netClip)">
      <rect x="290" y="10" width="619" height="668" fill="var(--panel)"/>
      <polygon points="290,330 909,40 909,250 290,500" fill="var(--panel-light)"/>
      <polygon points="290,500 909,250 909,420 290,640" fill="var(--panel-mid)"/>
      <polygon points="420,400 909,520 909,678 290,678" fill="#181818"/>
      <polygon points="290,284 757,120 757,140 290,320" fill="url(#goldBand)"/>
      <line x1="290" y1="320" x2="909" y2="90" stroke="#3a3a3a" stroke-width="1"/>
    </g>
    <line x1="599" y1="163" x2="757" y2="163" stroke="#333" stroke-width="1"/>
    <line x1="434" y1="163" x2="434" y2="678" stroke="#2c2c2c" stroke-width="1"/>
    <!-- flap rule -->
    <line x1="614" y1="83" x2="742" y2="83" stroke="var(--cream)" stroke-width="1"/>
    <line x1="304" y1="420" x2="424" y2="420" stroke="var(--cream)" stroke-width="1"/>
    <!-- front vertical rule -->
    <line x1="674" y1="190" x2="674" y2="490" stroke="var(--cream)" stroke-width="1.5"/>
    <!-- organic badge -->
    <rect x="773" y="276" width="77" height="43" fill="#8cbf26"/>
  </svg>

  <!-- decorative leaves -->
  <svg class="dieline" width="1200" height="800" viewBox="0 0 1200 800">
    <defs>
      <linearGradient id="leafTone" x1="0" y1="0" x2="0" y2="1">
        <stop offset="0" stop-color="#c07a14"/>
        <stop offset="1" stop-color="#e9c24a"/>
      </linearGradient>
    </defs>
    <rect x="290" y="485" width="70" height="105" rx="30" fill="url(#leafTone)" opacity="0.85" role="img" aria-label="Hanfblatt-Illustration in Gold"/>
    <rect x="636" y="645" width="74" height="33" rx="14" fill="url(#leafTone)" opacity="0.9" role="img" aria-label="Hanfblatt-Illustration in Gold"/>
  </svg>

  <!-- top flap -->
  <div class="t brand brand-flap">KORNWIESE</div>

  <!-- side panel -->
  <div class="t brand brand-side">KORNWIESE</div>
  <div class="t notice" style="left:465px; top:281px;">Dieses Produkt ist kein<br>Arzneimittel.</div>
  <div class="t notice" style="left:465px; top:340px;">zum Verzehr nicht<br>geeignet</div>
  <div class="t hint" style="left:464px; top:462px;">Vor Anwendung gut schütteln.<br>Trocken, kühl und lichtgeschützt<br>lagern.</div>
  <div class="t hint" style="left:464px; top:522px;">Nicht verwenden während der<br>Schwangerschaft und Stillzeit.</div>
  <div class="t hint" style="left:464px; top:567px;">Außerhalb der Reichweite von<br>Kindern aufbewahren.</div>
  <div class="t hint" style="left:464px; top:612px;">Vorsicht bei Hanfallergie.</div>
  <div class="t hint" style="left:464px; top:642px;">Geöffnet mindestens<br>3 Monate haltbar.</div>

  <!-- front panel -->
  <div class="t est-front"><span>EST. 2021</span></div>
  <div class="t brand brand-front"><span>KORNWIESE</span></div>

  <div class="claim-icon" style="left:776px; top:184px;"></div>
  <div class="t claim" style="left:805px; top:183px;">100 % Natürlich</div>
  <div class="claim-icon" style="left:776px; top:215px;"></div>
  <div class="t claim" style="left:805px; top:214px;">100 % Vegan</div>
  <svg class="claim-icon" style="left:776px; top:246px;" width="18" height="18" viewBox="0 0 18 18" aria-hidden="true">
    <path d="M4 9 L8 13 L14 5" fill="none" stroke="var(--gold)" stroke-width="2"/>
  </svg>
  <div class="t claim" style="left:805px; top:246px;">100 % Glutenfrei</div>

  <div class="t bullets" style="left:774px; top:327px;">
    <span>•</span>Biozertifiziert<br>
    <span>•</span>Voller Terpeneffekt<br>
    <span>•</span>Keine Konservierungsstoffe
  </div>

  <div class="t ingredients" style="left:779px; top:497px;">Inhaltsstoffe:<br>Bio Hanfsamenöl<br>(kaltgepresst)<br>Bio Hanfsamenextrakt</div>

  <div class="t premium" style="left:611px; top:548px;">Premium</div>
  <div class="t product" style="left:611px; top:561px;"><b>CBD</b> <em>Hanföl</em></div>
  <div class="t percent" style="left:611px; top:596px;">10%</div>
  <div class="t spectrum" style="left:674px; top:602px;">Das volle<br>Spektrum der<br>Hanfpflanze.</div>
  <div class="t volume" style="left:773px; top:645px;">10 ml</div>

  <!-- bottom flap -->
  <div class="t batch" style="left:614px; top:688px;">Charge:<br>Mindestens haltbar bis:</div>
  <div class="batch-field"></div>
</div>
</body>
</html>
```